Business Card Design For A Renovation Contractor Company

We need a business card for a new company based in Singapore, our company name is "KT Planora". We are a renovation contractor that builds designs into reality. We build more of F&B restaurants, retail stores and commercial offices. We work very closely with designers. The final design should communicate to our client that we are a company that you can trust, that will plan and complete your project without giving you a headache. I like my client to remember my company as "KT". The beauty of SIMPLE is important.

Industry/Entity Type

Contractor

Requirements
Nice to have
• Black or Red base

```html
<!DOCTYPE html>
<html lang="en">
<head>
<meta charset="UTF-8">
<title>KT Planora – Business Cards</title>
<link href="https://fonts.googleapis.com/css2?family=Questrial&family=Open+Sans:wght@400;700&display=swap" rel="stylesheet">
<style>
  :root {
    --backdrop: #e4e8ea;
    --paper: #ffffff;
    --brand-red: #e0272d;
    --red-edge: #c81f25;
    --charcoal: #2b2728;
    --charcoal-edge: #3a3637;
    --ink: #3b3b3b;
    --muted: #6d6d6d;
    --grid-light: #f7f7f7;
    --grid-mid: #ececec;
    --white: #ffffff;
  }
  * { margin: 0; padding: 0; box-sizing: border-box; }
  html, body { width: 1200px; height: 505px; overflow: hidden; }
  body {
    background: var(--backdrop);
    position: relative;
    font-family: "Open Sans", sans-serif;
  }
  .card {
    position: absolute;
    width: 322px;
    height: 171px;
    overflow: hidden;
  }
  .card--front { left: 76px; top: 125px; background: var(--paper); }
  .card--red { left: 436px; top: 129px; width: 320px; height: 170px; background: var(--brand-red); }
  .card--dark { left: 804px; top: 133px; height: 170px; background: var(--charcoal); }

  /* front */
  .front-mark {
    position: absolute; left: 52px; top: 12px;
    width: 38px; height: 38px; border-radius: 50%;
    border: 4px solid var(--ink);
  }
  .front-name {
    position: absolute; left: 16px; top: 50px;
    font-family: "Questrial", sans-serif;
    font-size: 21px; color: var(--ink); letter-spacing: -0.2px;
    white-space: nowrap;
  }
  .front-tagline {
    position: absolute; left: 16px; top: 76px; width: 122px;
    border-top: 1px solid var(--ink);
    font-family: "Questrial", sans-serif;
    font-size: 8px; color: var(--muted); padding-top: 1px;
    white-space: nowrap;
  }
  .contact-list {
    position: absolute; left: 17px; top: 95px;
    list-style: none; font-size: 9.5px; color: var(--ink);
  }
  .contact-list li { display: flex; align-items: center; height: 14.5px; }
  .contact-list svg { width: 8px; height: 8px; margin-right: 7px; fill: var(--brand-red); }
  .drawing-panel {
    position: absolute; left: 212px; top: 0; width: 110px; height: 171px;
    background: linear-gradient(90deg, var(--paper), var(--grid-light) 40%, var(--grid-mid));
  }
  .drawing-base {
    position: absolute; left: 10px; top: 164px; width: 300px; height: 4px;
    background: linear-gradient(90deg, var(--grid-light), var(--grid-mid));
  }
  .person {
    position: absolute; right: 22px; top: 77px; text-align: right;
  }
  .person-name { font-size: 11px; font-weight: 700; color: var(--brand-red); }
  .person-role { font-size: 9px; color: var(--charcoal); margin-top: 1px; }

  /* back cards */
  .ruler-strip {
    position: absolute; left: 0; top: 0; width: 14px; height: 100%;
  }
  .card--red .ruler-strip { background: var(--red-edge); }
  .card--dark .ruler-strip { background: linear-gradient(90deg, var(--charcoal-edge), #5a5657); }
  .back-block {
    position: absolute; left: 0; right: 0; top: 44px; text-align: center; color: var(--white);
  }
  .back-mark {
    width: 44px; height: 44px; border-radius: 50%;
    border: 4px solid var(--white); margin: 0 auto 4px;
  }
  .card--dark .back-mark { border-color: #d9d9d9; }
  .back-name {
    font-family: "Questrial", sans-serif; font-size: 23px; line-height: 1.05;
    white-space: nowrap;
  }
  .back-tagline {
    display: inline-block; border-top: 1px solid var(--white);
    font-family: "Questrial", sans-serif; font-size: 8.5px; padding: 0 8px;
    white-space: nowrap;
  }
  .back-url { font-size: 9.5px; letter-spacing: 0.8px; margin-top: 4px; }
</style>
</head>
<body>

  <section class="card card--front" aria-label="Business card front">
    <div class="drawing-panel" role="img" aria-label="Faint architectural grid with dimension lines"></div>
    <div class="drawing-base" role="img" aria-label="Horizontal dimension line"></div>
    <div class="front-mark"></div>
    <div class="front-name">KT Planora</div>
    <div class="front-tagline">from plan to finished space</div>
    <ul class="contact-list">
      <li><svg viewBox="0 0 10 10"><path d="M2 0l2 2.5-1 1.2c.6 1.3 1.6 2.3 2.9 2.9L7 5.5 10 7.5 8.7 9.7C4 9.5.4 6 .2 1.3z"/></svg>555.204.1187</li>
      <li><svg viewBox="0 0 10 10"><rect x="2" y="0" width="6" height="3"/><rect x="0" y="3.5" width="10" height="4"/><rect x="2" y="7.5" width="6" height="2.5"/></svg>555.204.1187</li>
      <li><svg viewBox="0 0 10 10"><path d="M0 2h10v6H0z M0 2l5 3.5L10 2" stroke="#fff" stroke-width=".8"/></svg>hello@ktplanora.com</li>
      <li><svg viewBox="0 0 10 10"><circle cx="5" cy="5" r="5"/><path d="M0 5h10M5 0v10" stroke="#fff" stroke-width=".8"/></svg>www.ktplanora.com</li>
    </ul>
    <div class="person">
      <div class="person-name">Mara Quill</div>
      <div class="person-role">Managing Director</div>
    </div>
  </section>

  <section class="card card--red" aria-label="Business card back, red">
    <div class="ruler-strip" role="img" aria-label="Ruler measurement strip"></div>
    <div class="back-block">
      <div class="back-mark"></div>
      <div class="back-name">KT Planora</div>
      <div class="back-tagline">from plan to finished space</div>
      <div class="back-url">www.ktplanora.com</div>
    </div>
  </section>

  <section class="card card--dark" aria-label="Business card back, charcoal">
    <div class="ruler-strip" role="img" aria-label="Ruler measurement strip"></div>
    <div class="back-block">
      <div class="back-mark"></div>
      <div class="back-name">KT Planora</div>
      <div class="back-tagline">from plan to finished space</div>
      <div class="back-url">www.ktplanora.com</div>
    </div>
  </section>

</body>
</html>
```